Multiple Banner-Ad Sets needed

We are a large insurance marketing program. We'd like to upgrade our display ads to be more effective.

We'd like to keep them provocative and scary like they are.

We need 5 sets of ads.
Each of the 5 sets shall include all 9 of the display ad sizes permitted by Vendrix PromoGrid.

3 of the sets need to be remade, but are attached as an example. The sets are:

Auto Insurance
Homeowners Insurance
Life Insurance
Business Insurance
Health Insurance

Target Market(s)

General public

Industry/Entity Type

Insurance

Font styles to use
Serif

Requirements
Must have
• Must be extremely provocative.

```html
<!DOCTYPE html>
<html lang="en">
<head>
<meta charset="utf-8">
<title>Health Insurance – Today Only</title>
<link rel="stylesheet" href="https://fonts.googleapis.com/css2?family=Noto+Serif:wght@700&display=swap">
<style>
  :root {
    --backdrop-light: #737373;
    --backdrop-mid: #3a3a3a;
    --backdrop-dark: #0c0c0c;
    --headline-white: #ffffff;
    --ribbon-light: #72c4ea;
    --ribbon-dark: #2478aa;
    --ribbon-edge: #0d3550;
    --ribbon-text: #14263a;
    --photo-top: #5e5048;
    --photo-mid: #8d7560;
    --photo-bottom: #c4a684;
  }
  html, body {
    margin: 0;
    padding: 0;
    width: 1200px;
    height: 2400px;
    overflow: hidden;
    background: var(--backdrop-dark);
  }
  .banner {
    position: relative;
    width: 1200px;
    height: 2400px;
    overflow: hidden;
    font-family: "Noto Serif", Georgia, serif;
    font-weight: 700;
    color: var(--headline-white);
  }
  .banner__backdrop {
    position: absolute;
    left: 0; top: 0;
    width: 1200px;
    height: 1448px;
    background: radial-gradient(ellipse 900px 1100px at 560px 420px,
      var(--backdrop-light) 0%, var(--backdrop-mid) 50%, var(--backdrop-dark) 100%);
  }
  .headline {
    position: absolute;
    left: 0;
    width: 1000px;
    margin: 0;
    text-align: center;
    font-size: 136px;
    line-height: 1;
    text-shadow: 0 6px 10px rgba(0,0,0,0.5);
  }
  .headline--health { top: 50px; }
  .headline--insurance { top: 248px; }
  .offer-ribbon {
    position: absolute;
    left: 0;
    top: 0;
    width: 1200px;
    height: 1000px;
  }
  .price {
    position: absolute;
    left: 0;
    width: 940px;
    margin: 0;
    text-align: center;
    font-size: 170px;
    line-height: 1;
    text-shadow: 0 6px 10px rgba(0,0,0,0.5);
  }
  .price--amount { top: 800px; }
  .price--per { top: 990px; }
  .price--month { top: 1180px; }
  .arena-photo {
    position: absolute;
    left: 0;
    top: 1448px;
    width: 1200px;
    height: 952px;
    background: linear-gradient(180deg, var(--photo-top) 0%, var(--photo-mid) 45%, var(--photo-bottom) 100%);
  }
</style>
</head>
<body>
  <main class="banner">
    <div class="banner__backdrop"></div>

    <h1 class="headline headline--health">HEALTH</h1>
    <h1 class="headline headline--insurance">INSURANCE</h1>

    <svg class="offer-ribbon" viewBox="0 0 1200 1000" aria-label="Today only">
      <defs>
        <linearGradient id="ribbonFill" x1="0" y1="0" x2="0" y2="1">
          <stop offset="0" stop-color="var(--ribbon-light)"/>
          <stop offset="1" stop-color="var(--ribbon-dark)"/>
        </linearGradient>
      </defs>
      <path d="M168 500 L1200 592 L1200 852 L156 742 Q134 738 137 716 L150 522 Q154 498 168 500 Z"
            fill="url(#ribbonFill)" stroke="var(--ribbon-edge)" stroke-width="4"/>
      <text x="710" y="728" text-anchor="middle" transform="rotate(6.5 710 690)"
            font-family="'Noto Serif', Georgia, serif" font-weight="700" font-size="100"
            fill="var(--ribbon-text)">TODAY ONLY</text>
    </svg>

    <p class="price price--amount">$30</p>
    <p class="price price--per">PER</p>
    <p class="price price--month">MONTH</p>

    <div class="arena-photo" role="img"
         aria-label="Photograph of a bullfighter being thrown by a charging bull in a sandy arena, crowd in the stands behind"></div>
  </main>
</body>
</html>
```